Menu Design Project for New Catering company

I would like to see my menus in a warm, inviting format. I prepare food for small intimate dinners, business lunches, picnics, parties, weddings and rehearsal dinners. I work with clients to help create their dream whether it includes items on my menu or to prepare very personal dishes that bring them warm memories of a special time or moment.

Target Market(s)

Organizations, wedding and or event planners

Industry/Entity Type

Catering

Requirements
Must have
• I would like to include the logo that is included in the attachment below. I also included a copy of the poster Lex Doyle created for me. I hope this helps. Please be creative. I am a very happy, cheerful person that enjoys cooking and having fun. I would like the design to represent my personality as well as my food. When I cater I treat my customers like an extension of my family and it comes across to them with everything I do for them. I hope this can somehow be reflected in your designs.
Should not have
• I'm open to all ideas and don't want to limit your creativity.

```html
<!DOCTYPE html>
<html lang="en">
<head>
<meta charset="utf-8">
<title>Catering Menu</title>
<link href="https://fonts.googleapis.com/css2?family=Montserrat:wght@800&family=Open+Sans:wght@300;400;600&display=swap" rel="stylesheet">
<style>
:root{
  --green:#1e8a3c;
  --green-soft:#4aa564;
  --ink:#4a4a4a;
  --ink-dark:#2b2b2b;
  --paper:#ffffff;
  --bg:#ffffff;
}
*{box-sizing:border-box;margin:0;padding:0}
html,body{width:1200px;height:5042px;overflow:hidden;background:var(--bg)}
body{position:relative;font-family:"Open Sans",Arial,sans-serif;color:var(--ink);font-weight:300}
.page{position:absolute;left:6px;width:1188px;background:var(--paper);border:9px solid var(--green)}
.page-one{top:0;height:1668px}
.page-two{top:1684px;height:1668px}
.page-three{top:3368px;height:1674px}

.brand{display:flex;flex-direction:column;align-items:center;color:var(--green);font-family:"Open Sans",Arial,sans-serif;font-weight:600}
.brand-mark{border:7px solid var(--green);border-radius:50%}
.brand-name{text-align:center;line-height:1.1}
.brand-small{position:absolute;left:60px;top:80px;width:320px}
.brand-small .brand-mark{width:110px;height:110px}
.brand-small .brand-name{font-size:34px;margin-top:16px}
.brand-large{position:absolute;left:0;right:0;top:1010px}
.brand-large .brand-mark{width:210px;height:210px}
.brand-large .brand-name{font-size:66px;margin-top:26px}

.menu-title{position:absolute;left:445px;top:85px;font-family:"Montserrat",Arial,sans-serif;font-weight:800;font-size:210px;letter-spacing:8px;line-height:1;color:transparent;-webkit-text-stroke:6px var(--green)}

.intro{position:absolute;left:70px;right:70px;top:395px;text-align:center;font-size:31px;line-height:1.32;font-weight:400;color:var(--ink-dark)}

.content{position:absolute;left:100px;right:95px;font-size:22.5px;line-height:1.3}
.page-one .content{top:650px}
.page-two .content{top:120px}
.page-three .content{top:125px}
.section-title{text-transform:uppercase;font-weight:400;color:var(--ink-dark);font-size:22.5px}
.section-title .note{float:right;text-transform:none;font-weight:300;color:var(--ink)}
.section{margin-bottom:30px}
.item{margin-bottom:6px}
.item-name{font-weight:400;color:var(--ink-dark)}
.price{float:right;color:var(--ink);white-space:nowrap}
.list{list-style:none}
.list li{overflow:hidden}
.lunch .item{margin-bottom:34px}
.lunch .item.tight{margin-bottom:20px}
</style>
</head>
<body>

<section class="page page-one">
  <div class="brand brand-small">
    <span class="brand-mark"></span>
    <span class="brand-name">Willow Spoon Catering</span>
  </div>
  <h1 class="menu-title">MENU</h1>
  <p class="intro">CATERED BUFFET SERVICES PROVIDED - We will arrive to your event prior to meal service, set-up and display your buffet including our buffet equipment. We will maintain your buffet keeping it clean and refreshed then depart immediately after meal service. Disposable dinnerware is included.</p>

  <div class="content">
    <div class="section">
      <h2 class="section-title">Buffet</h2>
      <p>Priced per person and includes - 1 Entree, 2 Sides or 1 Salad + 1 Side and a Dessert. Quotes to add additional entrée(s) and/or sides are available upon request or if you don't see exactly what you are looking for we will be happy to work with you to accommodate your requests. Appetizers and drinks are priced separately below.</p>
    </div>
    <div class="section">
      <h2 class="section-title">Entrees</h2>
      <p class="item"><span class="item-name">Lasagna Supreme Roll-up</span> – Lasagna noodles topped with ricotta, mozzarella and parmesan cheese, beef, sausage and pepperoni in a thick rich meat sauce <span class="price">- $12.00/person</span></p>
      <p class="item"><span class="item-name">Pork Tenderloin with Marsala Mushroom Sauce</span> – Tender lightly breaded pork tenderloin medallions topped with delicious sautéed mushrooms all simmered in Marsala wine and heavy cream to develop a rich, decadent sauce <span class="price">- $12.00/person</span></p>
      <p class="item"><span class="item-name">Smothered Chicken</span> – Honey mustard grilled chicken breast topped with sautéed mushrooms, crispy bacon, Monterey and cheddar cheese served with a creamy honey mustard sauce <span class="price">- $12.00/person</span></p>
      <p class="item"><span class="item-name">Hot Brown</span> – Sliced roast turkey seated atop toasted bread and smothered with a rich Mornay sauce—all broiled until golden brown and topped with crisp bacon strips and tomato <span class="price">- $12.00/person</span></p>
      <p class="item"><span class="item-name">Grandma's Bourbon Maple Glazed Ham</span> – Don't worry, you don't have to be 21 to enjoy this tender, juicy glazed ham <span class="price">- $10.00/person</span></p>
      <p class="item"><span class="item-name">Grilled or Smoked Chicken Breasts</span> – Cooked as requested, plain or glazed with a nice, sweet southern BBQ sauce <span class="price">- $10.00/person</span></p>
      <p class="item"><span class="item-name">Pulled Pork BBQ</span> – Tender smoked shredded pork in a sweet, spicy BBQ sauce, buns (onions and dill pickles on the side) <span class="price">- $10.00/person</span></p>
      <p class="item"><span class="item-name">Hawaiian Meatballs</span> – Beef meatballs, pineapple chunks, onions and peppers served in a sweet sauce served along with fluffy white rice side <span class="price">- $10.00/person</span></p>
    </div>
  </div>
</section>

<section class="page page-two">
  <div class="content">
    <div class="section">
      <h2 class="section-title">Salads:</h2>
      <p class="item"><span class="item-name">Chopped Salad</span> – Lettuce, Cinnamon Candied Pecans, Green Onions, Celery, Blue Cheese Vinaigrette and Blue Cheese Crumbles</p>
      <p class="item"><span class="item-name">Spinach Salad</span> – Fresh Spinach, Red Onions, Candied Pecans and Strawberries (when strawberries are available and/or in season)</p>
      <p class="item"><span class="item-name">House Salad</span> – Mixed Greens, Tomatoes, Carrots, Cucumbers, Croutons and Choice of two types of Dressing (Ranch, Honey Mustard, Italian, or Blue Cheese)</p>
    </div>
    <div class="section">
      <h2 class="section-title">Other Sides</h2>
      <ul class="list">
        <li>Broccoli Casserole</li>
        <li>Garlic Roasted Broccoli and Carrots</li>
        <li>Honey Glazed Carrots</li>
        <li>Macaroni Salad</li>
        <li>Old Fashioned Green Beans</li>
        <li>Pasta Salad</li>
        <li>Potato Salad</li>
        <li>Potatoes – Garlic Mashed, Scalloped, or Baked</li>
        <li>Southern Baked Beans</li>
        <li>Stewed Tomatoes</li>
        <li>Sweet &amp; Sour Slaw</li>
        <li>Sweet Corn (Creamed, Skillet Fried or Corn on the Cob)</li>
        <li>Sweet Potato Casserole</li>
      </ul>
    </div>
    <div class="section">
      <h2 class="section-title">Desserts</h2>
      <ul class="list">
        <li>Cheesecakes</li>
        <li>Cream Pies</li>
        <li>Cupcakes</li>
        <li>Fruit Pies</li>
        <li>Key Lime Pie</li>
      </ul>
    </div>
    <div class="section">
      <h2 class="section-title">Appetizers <span class="note">- Priced per appetizer/per person</span></h2>
      <ul class="list">
        <li>Sweet and Spicy Meatballs <span class="price">- $3.00/person</span></li>
        <li>Pinwheels (various) with salsas and/or dips <span class="price">- $3.00/person</span></li>
        <li>Stuffed Mushrooms <span class="price">- $3.00/person</span></li>
        <li>Mini fried chicken and waffles drizzled with maple syrup <span class="price">- $4.00/person</span></li>
        <li>Shrimp cocktails with cocktail sauce <span class="price">- $4.00/person</span></li>
      </ul>
    </div>
    <div class="section">
      <h2 class="section-title">Drinks <span style="text-transform:none">(includes cups and ice)</span></h2>
      <ul class="list">
        <li>12 oz. canned Soft Drinks <span class="price">- $1.00 Ea</span></li>
        <li>16 oz. bottled water <span class="price">- $1.00 Ea</span></li>
        <li>Gallon Tea (sweet or unsweetened) <span class="price">- $6.00 Ea</span></li>
      </ul>
    </div>
    <div class="section">
      <h2 class="section-title">Boxed Lunch Menu Options</h2>
      <p>Served with chips, choice of fruit cup or side salad, also included choice of cookie or cupcake. Drinks sold separately.</p>
      <p><span class="item-name">NOTE:</span> A delivery fee of $20.00 will be assessed for orders totaling less than $150.00. Please send your order to my e-mail address at least 24 Hours in advance also include time requested, address and contact information (including phone number) - I will send you a confirmation that the order has been received and invoiced day of delivery.</p>
    </div>
  </div>
</section>

<section class="page page-three">
  <div class="content lunch">
    <p class="item"><span class="item-name">Malibu Chicken</span> – Grilled chicken breast, topped with sweet honey baked ham, Swiss cheese and served on a fresh croissant with a side of rich sweet mustard sauce</p>
    <p class="item"><span class="item-name">Italian Meatball with Mozzarella Cheese</span> - In a rich marinara sauce served on a fresh Hoagie Bun</p>
    <p class="item"><span class="item-name">Grilled Hawaiian Chicken Sandwich</span> – Grilled chicken topped with a sweet grilled pineapple ring and guacamole sauce on a fresh Hawaiian bun or croissant</p>
    <p class="item"><span class="item-name">Honey Chicken Salad</span> – A fresh chicken salad filled with grapes, crispy celery, pecans, shredded chicken - served on a fresh croissant</p>
    <p class="item"><span class="item-name">Honey Baked Ham and Swiss Cheese</span> – piled high on a fresh croissant (with choices of - lettuce, tomato slice, onions and mayo/salad dressing)</p>
    <p class="item"><span class="item-name">Ultimate BLT with Avocado and Spicy Mayo</span> - Crispy bacon, lettuce, tomato, thin slices of red onion, avocado slices atop toasted bread with spicy mayo</p>
    <p class="item"><span class="item-name">Spinach Salad with Bacon Dressing</span> - Baby Spinach, mushrooms, red onions and sliced boiled eggs served with croissant and bacon dressing</p>
    <p class="item tight" style="margin-top:50px"><span class="item-name">Salad Dressing Choices</span> - Ranch, Italian, Honey Mustard or Blue Cheese</p>
    <p class="item"><span class="item-name">Drinks</span> - 12 oz. soft drinks or 16 oz. bottled water <span class="price">- $1.00 ea</span></p>
  </div>
  <div class="brand brand-large">
    <span class="brand-mark"></span>
    <span class="brand-name">Willow Spoon Catering</span>
  </div>
</section>

</body>
</html>
```